Interior designer needs business card design

I need a card for my new interior design company. I de sign mostly kitchens and baths, but don't want the card to list and specialty. I've gotten several clients already by Dordrecht of mouth, but now need to begin advertising.
I've got a pic of a silk screen used to print my father's old real estate sign and was hoping to use it as the basis for my card design.
Instead of "Sold by Marivone", I'd like the front of my card to read "Design by Marivone".
I like the font styles and banner and would like to stay as close to the original as possible, but with some twist--maybe color, not sure. Surprise me!
The back should list my email and phone
marivonedesign@quillpost.example
225-555-0193

```html
<!DOCTYPE html>
<html lang="en">
<head>
<meta charset="utf-8">
<title>Design by Marivone — Business Card</title>
<link href="https://fonts.googleapis.com/css2?family=Open+Sans:wght@400;700;800&display=swap" rel="stylesheet">
<style>
  :root {
    --backdrop: #e9e6e1;
    --card-white: #f8f7f4;
    --sage: #7fa197;
    --sunflower: #fcd651;
    --ink: #1f1f1f;
    --ink-soft: #333333;
    --white: #ffffff;
  }
  * { box-sizing: border-box; margin: 0; padding: 0; }
  html, body {
    width: 1200px;
    height: 844px;
    overflow: hidden;
    background: var(--backdrop);
    font-family: "Open Sans", Arial, sans-serif;
  }
  .sheet {
    position: relative;
    width: 1200px;
    height: 844px;
    display: flex;
    justify-content: center;
    align-items: center;
    gap: 100px;
  }
  .card {
    position: relative;
    width: 360px;
    height: 600px;
    border-radius: 20px;
    box-shadow: 0 10px 26px rgba(0,0,0,0.16);
    overflow: hidden;
  }
  .card--contact { background: var(--card-white); }
  .card--brand {
    background: var(--sunflower);
    display: flex;
    justify-content: center;
    align-items: center;
  }
  .wordmark {
    color: var(--sage);
    font-weight: 800;
    font-size: 46px;
    line-height: 1.05;
    text-transform: uppercase;
    text-align: center;
    letter-spacing: 0.02em;
  }
  .card--contact .wordmark {
    position: absolute;
    top: 62px;
    left: 0;
    right: 0;
  }
  .contact {
    position: absolute;
    left: 0;
    right: 0;
    top: 372px;
  }
  .contact__name {
    padding: 0 34px;
    font-weight: 700;
    font-size: 27px;
    letter-spacing: 0.05em;
    color: var(--ink);
    text-transform: uppercase;
  }
  .contact__phone {
    margin-top: 10px;
    background: var(--sunflower);
    color: var(--white);
    font-weight: 700;
    font-size: 34px;
    letter-spacing: 0.03em;
    padding: 4px 34px 6px;
    width: 328px;
  }
  .contact__email {
    margin-top: 12px;
    padding: 0 34px;
    font-weight: 400;
    font-size: 15px;
    color: var(--ink-soft);
    letter-spacing: 0.01em;
  }
</style>
</head>
<body>
  <main class="sheet">
    <section class="card card--contact" aria-label="Business card, contact side">
      <div class="wordmark">Design<br>by<br>Marivone</div>
      <div class="contact">
        <p class="contact__name">Teodor Marivone</p>
        <p class="contact__phone">225-555-0193</p>
        <p class="contact__email">marivonedesign@quillpost.example</p>
      </div>
    </section>

    <section class="card card--brand" aria-label="Business card, brand side">
      <div class="wordmark">Design<br>by<br>Marivone</div>
    </section>
  </main>
</body>
</html>
```